Essential Oil 15ml - package of 6

Design of a box of 6 different essential oils.
+ design of the bottle stickers
My bottles are 15ml clear blue glass.

The pictures attached are my competitors...

Target Market(s)

BRAMBLEWICK USA

Font styles to use
Serif

Requirements
Must have
• Our logo + "essential oil" and type (lavender, eucalyptus etc....)
• 15ml - 0.50 fl.oz.
• special color for the oil type.

```html
<!DOCTYPE html>
<html lang="en">
<head>
<meta charset="utf-8">
<title>Essential Oil 15ml – Bottle Labels</title>
<link rel="stylesheet" href="https://fonts.googleapis.com/css2?family=Kalam:wght@700&family=Roboto+Condensed:wght@400;700&display=swap">
<style>
  :root {
    --frame: #7a2636;
    --ink: #1a1a1a;
    --white: #ffffff;
    --lemon-1: #f58220; --lemon-2: #fdb515; --lemon-tint: #fed7a6;
    --mint-1: #6cc24a; --mint-2: #a8d84a; --mint-tint: #d3eeb0;
    --lav-1: #9a95e0; --lav-2: #b6b2ee; --lav-tint: #dcdaf6;
    --sage-1: #e65fd2; --sage-2: #f191e4; --sage-tint: #f8c8f1;
    --euc-1: #23b89a; --euc-2: #5fd3b8; --euc-tint: #b8ecdf;
    --frank-1: #a8631f; --frank-2: #e3a866; --frank-tint: #f6d9ae;
  }
  * { box-sizing: border-box; margin: 0; padding: 0; }
  html, body { width: 1200px; height: 885px; overflow: hidden; background: var(--white); }
  body { position: relative; font-family: "Roboto Condensed", Arial, sans-serif; color: var(--ink); }

  .label { position: absolute; width: 527px; height: 243px; }
  .label--lemon { left: 40px; top: 40px; --c1: var(--lemon-1); --c2: var(--lemon-2); --tint: var(--lemon-tint); }
  .label--mint { left: 567px; top: 40px; --c1: var(--mint-1); --c2: var(--mint-2); --tint: var(--mint-tint); }
  .label--lavender { left: 40px; top: 299px; --c1: var(--lav-1); --c2: var(--lav-2); --tint: var(--lav-tint); }
  .label--sage { left: 567px; top: 299px; --c1: var(--sage-1); --c2: var(--sage-2); --tint: var(--sage-tint); }
  .label--eucalyptus { left: 40px; top: 559px; --c1: var(--euc-1); --c2: var(--euc-2); --tint: var(--euc-tint); }
  .label--frank { left: 567px; top: 559px; --c1: var(--frank-1); --c2: var(--frank-2); --tint: var(--frank-tint); }

  .front { position: absolute; left: 0; top: 0; width: 280px; height: 100%;
    background: linear-gradient(90deg, var(--c1), var(--c2)); }
  .strip { position: absolute; left: 290px; top: 0; width: 20px; height: 100%; background: var(--tint); }
  .back { position: absolute; left: 310px; top: 0; width: 217px; height: 100%;
    background: linear-gradient(90deg, var(--white) 0%, var(--white) 55%, var(--tint) 85%, var(--c2) 100%); }
  .frame { position: absolute; left: 15px; top: 15px; width: 497px; height: 215px; border: 1px solid var(--frame); }

  .brand { position: absolute; left: 195px; top: 30px; width: 80px; text-align: center; }
  .brand__dot { display: block; width: 34px; height: 34px; margin: 0 auto 6px; border-radius: 50%; background: var(--ink); }
  .brand__name { font-size: 16px; font-weight: 400; color: var(--ink); }

  .oil-name { position: absolute; font-family: "Kalam", cursive; font-weight: 700; font-size: 50px; line-height: 1;
    color: var(--white); text-shadow: 1px 1px 0 var(--ink), 2px 2px 0 var(--ink), 3px 3px 0 var(--ink), -1px 0 0 var(--ink); }

  .rule { position: absolute; left: 130px; top: 200px; width: 135px; height: 1px; background: var(--white); }
  .volume { position: absolute; left: 35px; top: 196px; font-size: 11px; font-weight: 700; color: var(--white); }
  .purity { position: absolute; left: 130px; top: 204px; font-size: 11px; color: var(--white); opacity: .85; }

  .vert { position: absolute; writing-mode: vertical-rl; transform: rotate(180deg); text-align: center; }
  .strip-name { left: 293px; top: 22px; height: 90px; font-size: 12px; color: var(--white); text-align: end; letter-spacing: .5px; }
  .desc { left: 312px; top: 25px; width: 66px; height: 193px; border: 1.5px solid var(--c2); background: var(--white);
    font-size: 12px; line-height: 16px; padding: 4px 0; display: flex; align-items: center; }
  .company { left: 384px; top: 20px; width: 32px; height: 200px; font-size: 12px; line-height: 15px; }
  .grade { left: 418px; top: 20px; width: 22px; height: 200px; font-size: 8.5px; line-height: 11px; }
  .caution { left: 453px; top: 20px; width: 48px; height: 200px; font-size: 8.5px; line-height: 11px; }
</style>
</head>
<body>

<section class="label label--lemon">
  <div class="front"></div><div class="strip"></div><div class="back"></div><div class="frame"></div>
  <div class="brand"><span class="brand__dot"></span><span class="brand__name">Sela Spring</span></div>
  <div class="oil-name" style="left:32px;top:128px">Lemon</div>
  <div class="rule"></div><div class="volume">15ml</div><div class="purity">100% Pure Essential Oil</div>
  <div class="vert strip-name">LEMON</div>
  <div class="vert desc">The Detox oil use for sore throat seasonal discomfort, balancing PH levels, gout, kidney stones and to uplift mood.</div>
  <div class="vert company">Sela Spring Botanicals Ltd.<br>P.O. Box 4021 Harbor City 90710 USA</div>
  <div class="vert grade">For Aromatic, topical use. 100% Pure therapeutic grade essential oil.</div>
  <div class="vert caution">CAUTION : For external Use Only. Not for ingestion. Keep away from eyes and mucus membrane. May cause skin sensitivity. Keep out of reach of children. Keep away fro flame</div>
</section>

<section class="label label--mint">
  <div class="front"></div><div class="strip"></div><div class="back"></div><div class="frame"></div>
  <div class="brand"><span class="brand__dot"></span><span class="brand__name">Sela Spring</span></div>
  <div class="oil-name" style="left:30px;top:92px">Pepper</div>
  <div class="oil-name" style="left:130px;top:138px">mint</div>
  <div class="rule"></div><div class="volume">15ml</div><div class="purity">100% Pure Essential Oil</div>
  <div class="vert strip-name">PEPPERMINT</div>
  <div class="vert desc">The cooling oil used for respiratory issue, digestive, discomfort, pain, headache, fevers, acid reflux and to flavour food</div>
  <div class="vert company">Sela Spring Botanicals Ltd.<br>P.O. Box 4021 Harbor City 90710 USA</div>
  <div class="vert grade">For Aromatic, topical use. 100% Pure therapeutic grade essential oil.</div>
  <div class="vert caution">CAUTION : For external Use Only. Not for ingestion. Keep away from eyes and mucus membrane. May cause skin sensitivity. Keep out of reach of children. Keep away fro flame</div>
</section>

<section class="label label--lavender">
  <div class="front"></div><div class="strip"></div><div class="back"></div><div class="frame"></div>
  <div class="brand"><span class="brand__dot"></span><span class="brand__name">Sela Spring</span></div>
  <div class="oil-name" style="left:32px;top:128px">Lavender</div>
  <div class="rule"></div><div class="volume">15ml</div><div class="purity">100% Pure Essential Oil</div>
  <div class="vert strip-name">PEPPERMINT</div>
  <div class="vert desc">The Calming Oil use on irritated skin for muscle tension headache to calm and relax the mind and reduce stress and to promote restful sleep</div>
  <div class="vert company">Sela Spring Botanicals Ltd.<br>P.O. Box 4021 Harbor City 90710 USA</div>
  <div class="vert grade">For Aromatic, topical use. 100% Pure therapeutic grade essential oil.</div>
  <div class="vert caution">CAUTION : For external Use Only. Not for ingestion. Keep away from eyes and mucus membrane. May cause skin sensitivity. Keep out of reach of children. Keep away fro flame</div>
</section>

<section class="label label--sage">
  <div class="front"></div><div class="strip"></div><div class="back"></div><div class="frame"></div>
  <div class="brand"><span class="brand__dot"></span><span class="brand__name">Sela Spring</span></div>
  <div class="oil-name" style="left:30px;top:76px">Clary</div>
  <div class="oil-name" style="left:118px;top:130px">sage</div>
  <div class="rule"></div><div class="volume">15ml</div><div class="purity">100% Pure Essential Oil</div>
  <div class="vert strip-name">PEPPERMINT</div>
  <div class="vert desc">Use for depression, anxiety, hot flashers stress, balancing hormones, inflammation PMS, cramps, infertility and to uplift mood.</div>
  <div class="vert company">Sela Spring Botanicals Ltd.<br>P.O. Box 4021 Harbor City 90710 USA</div>
  <div class="vert grade">For Aromatic, topical use. 100% Pure therapeutic grade essential oil.</div>
  <div class="vert caution">CAUTION : For external Use Only. Not for ingestion. Keep away from eyes and mucus membrane. May cause skin sensitivity. Keep out of reach of children. Keep away fro flame</div>
</section>

<section class="label label--eucalyptus">
  <div class="front"></div><div class="strip"></div><div class="back"></div><div class="frame"></div>
  <div class="brand"><span class="brand__dot"></span><span class="brand__name">Sela Spring</span></div>
  <div class="oil-name" style="left:30px;top:128px;font-size:46px">Eucalyptus</div>
  <div class="rule"></div><div class="volume">15ml</div><div class="purity">100% Pure Essential Oil</div>
  <div class="vert strip-name">PEPPERMINT</div>
  <div class="vert desc">Use for coughs, asthma, congestion, respiratory issues, sinusitis, bronchitis, allergies, pneumonia, joint pain, and hot flashes</div>
  <div class="vert company">Sela Spring Botanicals Ltd.<br>P.O. Box 4021 Harbor City 90710 USA</div>
  <div class="vert grade">For Aromatic, topical use. 100% Pure therapeutic grade essential oil.</div>
  <div class="vert caution">CAUTION : For external Use Only. Not for ingestion. Keep away from eyes and mucus membrane. May cause skin sensitivity. Keep out of reach of children. Keep away fro flame</div>
</section>

<section class="label label--frank">
  <div class="front"></div><div class="strip"></div><div class="back"></div><div class="frame"></div>
  <div class="brand"><span class="brand__dot"></span><span class="brand__name">Sela Spring</span></div>
  <div class="oil-name" style="left:28px;top:130px;font-size:44px">Frankincense</div>
  <div class="rule"></div><div class="volume">15ml</div><div class="purity">100% Pure Essential Oil</div>
  <div class="vert strip-name">PEPPERMINT</div>
  <div class="vert desc">The Detox oil use for sore throat seasonal discomfort, balancing PH levels, gout, kidney stones and to uplift mood.</div>
  <div class="vert company">Sela Spring Botanicals Ltd.<br>P.O. Box 4021 Harbor City 90710 USA</div>
  <div class="vert grade">For Aromatic, topical use. 100% Pure therapeutic grade essential oil.</div>
  <div class="vert caution">CAUTION : For external Use Only. Not for ingestion. Keep away from eyes and mucus membrane. May cause skin sensitivity. Keep out of reach of children. Keep away fro flame</div>
</section>

</body>
</html>
```